business card with 2 locations on 1 card

I need a modern looking business card that I would use at 2 different locations. Possibly 1 location on 1 side and other location on other side. One should be able to distinguish the 2 locations immediately before having to read the address or description on card. You can take a look at my website to see what I'm drawn to. The logo is brand new that I just purchased on Craft Hive. I want to emphasize family.
Updates

Let's not use the yellow and blue colors. Added Thursday, August 31, 2017

Target Market(s)

women and children

Industry/Entity Type

Health And Wellness

Contact Information for Business Card

Business name: Willow Brook Chiropractic & Acupuncture
My name: Lorin Daske
Job title: DC, MAOM, LAc (CA), CNS

Location 1
Address: 4817 Marlowe Blvd, Suite B-100, Frisco, TX 75034
Phone: (469) 555-0182
Fax: (972) 555-0137

Location 2
Address: 1936 Belvane Road, Suite 100, Plano, TX 75075
Phone: (469) 555-0169
Fax: (972) 555-0137

Email: drlorindaske@mailnest.example
Website: www.drlorindaske.example

Font styles to use
Serif
Sans Serif

Colors

Designer to choose colors to be used in the design.

Requirements
Must have
• distinction between 2 locations.
Nice to have
• Colors preference below is there. But I like to see what you come up with too!

```html
<!DOCTYPE html>
<html lang="en">
<head>
<meta charset="utf-8">
<title>Willow Brook Chiropractic &amp; Acupuncture – Business Card</title>
<link href="https://fonts.googleapis.com/css2?family=Open+Sans:wght@400;600;700&display=swap" rel="stylesheet">
<style>
  :root {
    --teal: #246a68;
    --teal-dark: #1d5b59;
    --leaf-light: #8cc866;
    --leaf-dark: #1d8a2c;
    --paper: #fbfbfb;
    --ink: #2b2b2b;
    --backdrop: #e6e7e6;
  }
  * { margin: 0; padding: 0; box-sizing: border-box; }
  html, body { width: 1200px; height: 904px; overflow: hidden; }
  body {
    background: var(--backdrop);
    font-family: "Open Sans", Arial, sans-serif;
    display: flex; flex-direction: column; align-items: center; justify-content: center;
    gap: 44px;
  }
  .card {
    width: 700px; height: 400px; position: relative;
    box-shadow: 0 6px 18px rgba(0,0,0,.18);
    overflow: hidden;
  }
  .card--front { background: var(--teal); color: #fff; display: flex; align-items: center; justify-content: center; }
  .card--back { background: var(--paper); color: var(--ink); text-align: center; }

  .brand { display: flex; flex-direction: column; align-items: center; gap: 14px; }
  .brand__mark { width: 96px; height: 96px; border-radius: 50%; border: 5px solid currentColor; }
  .brand__name {
    font-weight: 600; font-size: 26px; line-height: 1.2; letter-spacing: .5px; text-align: center;
  }
  .card--front .brand__name { color: #fff; }
  .card--back .brand { margin-top: 30px; gap: 10px; color: var(--teal); }
  .card--back .brand__mark { width: 70px; height: 70px; border-width: 4px; }
  .card--back .brand__name { font-size: 19px; color: var(--teal); }

  .person__name { margin-top: 16px; font-size: 24px; font-weight: 700; color: var(--teal); }
  .person__title { font-size: 14px; color: #444; margin-top: 2px; }

  .contact { margin-top: 22px; font-size: 13.5px; line-height: 1.65; color: var(--ink); }
  .contact__sep { color: #777; margin: 0 5px; }
  .icon { width: 12px; height: 12px; vertical-align: -1px; margin-right: 3px; }
  .icon * { fill: none; stroke: var(--teal); stroke-width: 2; stroke-linecap: round; stroke-linejoin: round; }

  .stripe { position: absolute; left: 0; right: 0; bottom: 0; height: 12px; display: flex; }
  .stripe__seg--teal { flex: 1; background: var(--teal-dark); }
  .stripe__seg--light { flex: 1; background: var(--leaf-light); }
  .stripe__seg--dark { flex: 1; background: var(--leaf-dark); }
</style>
</head>
<body>
  <section class="card card--front">
    <div class="brand">
      <div class="brand__mark"></div>
      <div class="brand__name">Willow Brook<br>Chiropractic &amp; Acupuncture</div>
    </div>
  </section>

  <section class="card card--back">
    <div class="brand">
      <div class="brand__mark"></div>
      <div class="brand__name">Willow Brook<br>Chiropractic &amp; Acupuncture</div>
    </div>
    <h1 class="person__name">Lorin Daske</h1>
    <p class="person__title">DC, MAOM, LAc (CA), CNS</p>
    <div class="contact">
      <p>4817 Marlowe Blvd, Suite B-100, Frisco, TX 75034<span class="contact__sep">|</span><svg class="icon" viewBox="0 0 12 12"><path d="M3 1l2 2-1 1.5q1 2.5 3.5 3.5L9 7l2 2-1.5 2Q4 10 1 2.5z"/></svg>(469) 555-0182<span class="contact__sep">|</span><svg class="icon" viewBox="0 0 12 12"><rect x="1.5" y="5" width="9" height="5.5" rx="1"/><path d="M3.5 5V1.5h5V5"/></svg>(972) 555-0137</p>
      <p>1936 Belvane Road, Suite 100, Plano, TX 75075<span class="contact__sep">|</span><svg class="icon" viewBox="0 0 12 12"><path d="M3 1l2 2-1 1.5q1 2.5 3.5 3.5L9 7l2 2-1.5 2Q4 10 1 2.5z"/></svg>(469) 555-0169<span class="contact__sep">|</span><svg class="icon" viewBox="0 0 12 12"><rect x="1.5" y="5" width="9" height="5.5" rx="1"/><path d="M3.5 5V1.5h5V5"/></svg>(972) 555-0137</p>
      <p><svg class="icon" viewBox="0 0 12 12"><rect x="1" y="2.5" width="10" height="7" rx="1"/><path d="M1 3l5 4 5-4"/></svg>drlorindaske@mailnest.example<span class="contact__sep">|</span><svg class="icon" viewBox="0 0 12 12"><circle cx="6" cy="6" r="5"/><path d="M1 6h10M6 1q-3 5 0 10M6 1q3 5 0 10"/></svg>www.drlorindaske.example</p>
    </div>
    <div class="stripe">
      <span class="stripe__seg--teal"></span>
      <span class="stripe__seg--light"></span>
      <span class="stripe__seg--dark"></span>
    </div>
  </section>
</body>
</html>
```